Marlowe Hairdressing Business Card Design

The design has to be based upon a colour scheme of a black gloss background and silver type face letters and has to portray an exclusive and expensive outlet.

The business card has a dual use with the rear of the card being used for future appointments therefore this area has to be lined out to accept written text.

We also need to incorporate a Chatterbook log somewhere on the card.

Target Market(s)

High Earning individuals with high disposable incomes possible link too young professionals.

Contact Information for Business Card

Marlowe Hairdressing & The Willowmere Beauty
Tel 01632 418550
www.marlowehairdressing.example.co.uk

Requirements
Must have
• Company Name including beauty element, telephone number, website and chatterbook please.
Nice to have
• High Gloss finish with silver raised letters or similar
Should not have
• Hairdressing Images like, scissors, haircuts, beauty treatments etc

```html
<!DOCTYPE html>
<html lang="en">
<head>
<meta charset="utf-8">
<title>Marlowe Hairdressing – Business Card</title>
<link rel="stylesheet" href="https://fonts.googleapis.com/css2?family=Quicksand:wght@400;500&display=swap">
<style>
  :root {
    --page-bg: #e4e4e6;
    --card-black: #050505;
    --band-dark: #151515;
    --band-light: #242424;
    --silver: #c9c9c9;
    --silver-dim: #8e8e8e;
    --silver-text: #e6e6e6;
    --note-paper: #e8e8e8;
    --note-line: #3a3a3a;
    --card-font: "Quicksand", sans-serif;
  }
  * { box-sizing: border-box; margin: 0; padding: 0; }
  html, body { width: 1200px; height: 1200px; overflow: hidden; }
  body {
    background: radial-gradient(circle at 50% 40%, #f2f2f3, var(--page-bg) 70%);
    font-family: var(--card-font);
    display: flex;
    flex-direction: column;
    align-items: center;
    justify-content: center;
    gap: 60px;
  }
  .card {
    position: relative;
    width: 780px;
    height: 500px;
    background: var(--card-black);
    box-shadow: 0 10px 30px rgba(0,0,0,0.28);
    overflow: hidden;
  }
  .card-frame {
    position: absolute;
    inset: 28px;
    border: 3px solid var(--silver);
    box-shadow: 0 0 0 1px #555, inset 0 0 0 1px #555;
  }

  /* Front */
  .front {
    background: linear-gradient(180deg, #0a0a0a 0%, #1b1b1b 45%, #060606 100%);
  }
  .title-band {
    position: absolute;
    left: 0; right: 0;
    top: 120px;
    height: 150px;
    background: linear-gradient(180deg, var(--band-light), var(--band-dark) 55%, #0c0c0c);
    border-top: 1px solid #2e2e2e;
  }
  .company-name {
    position: absolute;
    left: 60px;
    top: 150px;
    color: var(--silver-text);
    font-size: 42px;
    font-weight: 400;
    line-height: 1.08;
    letter-spacing: 1.5px;
  }
  .phone {
    position: absolute;
    right: 62px;
    top: 296px;
    color: var(--silver-text);
    font-size: 22px;
    font-weight: 500;
    letter-spacing: 2px;
  }
  .holder {
    position: absolute;
    left: 72px;
    top: 335px;
    color: var(--silver-text);
    font-size: 27px;
    line-height: 1.3;
    letter-spacing: 1.5px;
  }
  .website {
    position: absolute;
    left: 0; right: 0;
    text-align: center;
    color: var(--silver);
    font-size: 24px;
    letter-spacing: 2.5px;
  }
  .front .website { bottom: 36px; }

  /* Back */
  .appointment-area {
    position: absolute;
    left: 34px; right: 34px;
    top: 34px;
    height: 340px;
    background: var(--note-paper);
    display: flex;
    flex-direction: column;
    justify-content: space-evenly;
    padding: 6px 0;
  }
  .write-line {
    height: 1.5px;
    background: var(--note-line);
  }
  .back-band {
    position: absolute;
    left: 34px; right: 34px;
    top: 374px;
    height: 92px;
    background: var(--card-black);
  }
  .back .website { top: 402px; color: var(--silver); }
</style>
</head>
<body>
  <section class="card front" aria-label="Business card front">
    <div class="title-band"></div>
    <div class="card-frame"></div>
    <h1 class="company-name">Marlowe Hairdressing &amp;<br>The Willowmere Beauty</h1>
    <p class="phone">Tel 01632 418550</p>
    <p class="holder">Daniel Hartley<br>Job Title</p>
    <p class="website">www.marlowehairdressing.example.co.uk</p>
  </section>

  <section class="card back" aria-label="Business card back, appointment lines">
    <div class="card-frame"></div>
    <div class="appointment-area">
      <div class="write-line"></div>
      <div class="write-line"></div>
      <div class="write-line"></div>
      <div class="write-line"></div>
      <div class="write-line"></div>
      <div class="write-line"></div>
      <div class="write-line"></div>
      <div class="write-line"></div>
    </div>
    <div class="back-band"></div>
    <p class="website">www.marlowehairdressing.example.co.uk</p>
  </section>
</body>
</html>
```